" Window Blinds and Shutters Business Card Design"

We require a business card design for a new windows blinds and shutters company based in Sydney.
The business name is 'Larkvale Blinds and Shutters'.
We supply and install homes and businesses with internal and external window furnishings and finishes. This includes varieties of window blinds and window shutters.

Benefits of Larkvale Blinds and Shutters :
Added security and privacy,
The ability to control the amount of sunlight,
Regulate internal temperature.

Blinds varieties:
Roller Blinds, Double Roller Blinds, Roman Blinds, Vertical Blinds, Aluminium venetians, Timber venetians and PVC Venetians.

Shutters varieties:
Plantation Shutters, Aluminium Louvre Shutters, Roller Shutters and Security Shutters .
Updates

Hi Designers,

Please have a look at my Business card design brief. I need your help to start my new business.

Thanks,

Dorian.

Reason: not 100% happy with the options available, close to 90% happy, need a little more refinement. Thank You & Good Luck

Target Market(s)

Home owners, business owners, shift workers , and new home builders.

Industry/Entity Type

Security

Contact Information for Business Card

Larkvale Blinds and Shutters,

Dorian Kettlewell mobile: 0487561904,
Priya Hensworth mobile: 0472846015,

email: dorian.kettlewell@mailgrove.net
web: larkvaleblindsandshutters.com.au

Colors
ffffff
9d9d9d
f78f20

Requirements
Must have
• ON FRONT OF CARD
I have attached a picture of logo and need a designer to design a font logo for Larkvale Blinds and Shutters similar, or open to suggestions.

FRONT OF CARD
Company message/:
"Sheltering windows with style"

BACK OF CARD
'For a FREE measure & quote call Dorian - 0487561904"
Nice to have
• Elegant yet professional.

Soft colours appealing to both male & female clients.

Should not have

• Unprofessional fonts

```html
<!DOCTYPE html>
<html lang="en">
<head>
<meta charset="utf-8">
<title>Larkvale Blinds and Shutters – Business Card</title>
<link rel="stylesheet" href="https://fonts.googleapis.com/css2?family=Cinzel:wght@400;600;700&family=Federo&display=swap">
<style>
  :root {
    --brand-red: #e1262c;
    --contact-blue: #1e58a6;
    --ink: #111111;
    --blind-light: #fbfbfb;
    --blind-mid: #ececec;
    --blind-shade: #dcdcdc;
  }
  html, body {
    margin: 0;
    padding: 0;
    width: 1200px;
    height: 741px;
    overflow: hidden;
    background: #ffffff;
  }
  .card {
    position: relative;
    width: 1200px;
    height: 741px;
    overflow: hidden;
  }
  .card__backdrop {
    position: absolute;
    inset: 0;
    background:
      linear-gradient(180deg, var(--blind-light) 0%, var(--blind-light) 20%, var(--blind-mid) 22%, var(--blind-light) 30%, var(--blind-mid) 55%, var(--blind-light) 75%, var(--blind-shade) 100%),
      var(--blind-light);
  }
  .card__content {
    position: absolute;
    inset: 0;
  }
  .centered {
    position: absolute;
    left: 0;
    width: 100%;
    text-align: center;
    margin: 0;
    white-space: nowrap;
  }
  .brand-mark {
    top: 55px;
    font-family: "Federo", sans-serif;
    font-size: 148px;
    line-height: 1;
    color: var(--brand-red);
    letter-spacing: 4px;
  }
  .business-name {
    top: 201px;
    font-family: "Federo", sans-serif;
    font-weight: 400;
    font-size: 68px;
    line-height: 1;
    color: var(--brand-red);
    letter-spacing: 1px;
    font-variant: small-caps;
    text-shadow: 2px 3px 3px rgba(0,0,0,0.35);
  }
  .tagline {
    top: 304px;
    font-family: "Cinzel", serif;
    font-weight: 700;
    font-size: 36px;
    line-height: 1;
    color: var(--ink);
    letter-spacing: 2px;
  }
  .contact-person {
    position: absolute;
    top: 452px;
    width: 420px;
    text-align: center;
    font-family: "Cinzel", serif;
    white-space: nowrap;
  }
  .contact-person--primary { left: 163px; }
  .contact-person--secondary { left: 683px; }
  .contact-person__name {
    display: block;
    font-weight: 700;
    font-size: 27px;
    line-height: 1;
    color: var(--contact-blue);
    letter-spacing: 1px;
  }
  .contact-person__phone {
    display: block;
    margin-top: 28px;
    font-weight: 400;
    font-size: 34px;
    line-height: 1;
    color: var(--brand-red);
    letter-spacing: 1px;
  }
  .web-details {
    font-family: "Cinzel", serif;
    font-weight: 700;
    font-size: 28px;
    line-height: 1;
    color: var(--ink);
    letter-spacing: 1px;
    text-transform: uppercase;
  }
  .web-details--email { top: 588px; }
  .web-details--site { top: 636px; }
</style>
</head>
<body>
  <main class="card">
    <div class="card__backdrop" role="img" aria-label="Close-up photo of white window blind slats filling the card background"></div>
    <div class="card__content">
      <p class="centered brand-mark">LBS</p>
      <h1 class="centered business-name">Larkvale Blinds and Shutters</h1>
      <p class="centered tagline">Sheltering windows with style</p>

      <div class="contact-person contact-person--primary">
        <span class="contact-person__name">Dorian Kettlewell</span>
        <span class="contact-person__phone">0487561904</span>
      </div>
      <div class="contact-person contact-person--secondary">
        <span class="contact-person__name">Priya Hensworth</span>
        <span class="contact-person__phone">0472846015</span>
      </div>

      <p class="centered web-details web-details--email">dorian.kettlewell@mailgrove.net</p>
      <p class="centered web-details web-details--site">larkvaleblindsandshutters.com.au</p>
    </div>
  </main>
</body>
</html>
```